Brisk Tailor Signage

This design is for "signage" that we intend to get produced.
A couple of different designs that say "Brisk Tailor on Guard" and "Beware of Brisk Tailor"
It should also have our logo (BT) plus our logo with the hand and dog paw. We would also like the main picture of the sign to be the attached. We would like a classy sophisticated look similar to our logo you designed.
Our designs will go on consumers gates/entrances to warn people there is a dog on the premises. I will get a better quality picture of the dog.

```html
<!DOCTYPE html>
<html lang="en">
<head>
<meta charset="utf-8">
<title>Brisk Tailor – Beware Sign</title>
<link rel="stylesheet" href="https://fonts.googleapis.com/css2?family=Pinyon+Script&family=Great+Vibes&family=Cinzel:wght@400&display=swap">
<style>
  :root {
    --backdrop: #b5b5b5;
    --sign-white: #ffffff;
    --ring-lavender: #a2abe3;
    --ink: #1a1a1a;
    --script-blue: #8fa2d6;
    --dog-blue: #5681bb;
  }
  html, body {
    margin: 0;
    padding: 0;
    width: 1200px;
    height: 1200px;
    overflow: hidden;
    background: var(--backdrop);
  }
  .canvas {
    position: relative;
    width: 1200px;
    height: 1200px;
  }
  .sign {
    position: absolute;
    left: 202px;
    top: 202px;
    width: 796px;
    height: 796px;
    border-radius: 50%;
    background: var(--sign-white);
    box-shadow: 0 2px 6px rgba(0,0,0,0.25);
  }
  .sign-ring {
    position: absolute;
    left: 224px;
    top: 224px;
    width: 736px;
    height: 736px;
    border-radius: 50%;
    border: 8px solid var(--ring-lavender);
  }
  .brand-lockup {
    position: absolute;
    left: 362px;
    top: 326px;
    display: flex;
    align-items: center;
    gap: 14px;
  }
  .brand-dot {
    width: 84px;
    height: 84px;
    border-radius: 50%;
    border: 3px solid var(--ring-lavender);
    box-sizing: border-box;
  }
  .brand-name {
    font-family: "Pinyon Script", cursive;
    font-size: 72px;
    line-height: 1;
    color: var(--ink);
    white-space: nowrap;
  }
  .guard-dog {
    position: absolute;
    left: 516px;
    top: 432px;
  }
  .headline {
    position: absolute;
    left: 0;
    width: 1200px;
    text-align: center;
    margin: 0;
  }
  .headline-beware {
    top: 680px;
    font-family: "Great Vibes", cursive;
    font-size: 150px;
    line-height: 1;
    color: var(--script-blue);
  }
  .headline-of {
    top: 818px;
    font-family: "Cinzel", serif;
    font-size: 40px;
    line-height: 1;
    color: var(--ink);
    left: -8px;
  }
  .headline-name {
    top: 857px;
    font-family: "Cinzel", serif;
    font-size: 52px;
    line-height: 1;
    color: var(--ink);
    letter-spacing: 1px;
  }
</style>
</head>
<body>
<main class="canvas">
  <div class="sign"></div>
  <div class="sign-ring"></div>

  <div class="brand-lockup">
    <div class="brand-dot"></div>
    <span class="brand-name">Brisk Tailor</span>
  </div>

  <svg class="guard-dog" width="196" height="300" viewBox="0 0 196 300" role="img" aria-label="Illustration of a seated blue low-poly guard dog">
    <rect x="0" y="0" width="196" height="300" rx="12" fill="var(--dog-blue)"/>
  </svg>

  <p class="headline headline-beware">Beware</p>
  <p class="headline headline-of">OF</p>
  <p class="headline headline-name">Brisk Tailor</p>
</main>
</body>
</html>
```